A new presentation to our clients

we are a Real Estate agency, our website is www.dorelumia.com and it’s time to have a new, fashion and remarcable Business Card. we want to differentiate ourselves from other companies so we want a business card that differentiates us. we want the business card to impact our customers. in the competitive market that we have today, we have to be different and it is this difference that we seek

Target Market(s)

Real Estate Clients

Contact Information for Business Card

We search a totaly diferent card from the usual

Font styles to use
Sans Serif

Colors
e34197

Requirements
Must have
• Logo, adress, phone contact, e-mail, photo, and our website
Nice to have
• We would like to see a modern business card
Should not have
• Houses or building draws

```html
<!DOCTYPE html>
<html lang="en">
<head>
<meta charset="utf-8">
<title>Dore Lumia – Business Card</title>
<link rel="stylesheet" href="https://fonts.googleapis.com/css2?family=Questrial&family=Nunito+Sans:wght@700&display=swap">
<style>
  :root {
    --backdrop: #ece8e4;
    --brand-pink: #e34197;
    --brand-pink-deep: #dc2a83;
    --brand-pink-light: #ee5fae;
    --logo-tint: #f7c9e2;
    --ink-white: #ffffff;
    --ink-soft: #fde9f3;
    --portrait-navy: #2a3555;
  }
  * { margin: 0; padding: 0; box-sizing: border-box; }
  html, body { width: 900px; height: 1200px; overflow: hidden; }
  body {
    background: var(--backdrop);
    font-family: "Questrial", "Century Gothic", sans-serif;
    position: relative;
  }
  .card {
    position: absolute;
    left: 82px;
    width: 740px;
    height: 432px;
    overflow: hidden;
    box-shadow: 0 6px 14px rgba(0,0,0,0.25);
  }
  .card--front {
    top: 125px;
    border-radius: 46px 0 46px 0;
    background: linear-gradient(180deg, var(--brand-pink-deep) 0%, var(--brand-pink) 100%);
  }
  .card--back {
    top: 640px;
    border-radius: 0 46px 0 46px;
    background: var(--brand-pink);
  }
  .brand-name {
    position: absolute;
    font-family: "Questrial", sans-serif;
    font-size: 70px;
    line-height: 1;
    letter-spacing: 1px;
    white-space: nowrap;
  }
  .card--front .brand-name { left: 54px; top: 56px; color: var(--ink-white); }
  .card--back .brand-name {
    left: 0; right: 0; top: 188px; text-align: center; color: var(--logo-tint);
  }
  .holder { position: absolute; left: 56px; top: 163px; color: var(--ink-white); }
  .holder__name {
    font-family: "Nunito Sans", sans-serif;
    font-weight: 700;
    font-size: 20px;
    letter-spacing: 0.3px;
  }
  .holder__role { font-size: 15px; margin-top: 3px; }
  .address {
    position: absolute; left: 56px; top: 226px;
    color: var(--ink-soft); font-size: 16px; line-height: 27px;
  }
  .contacts {
    position: absolute; left: 56px; top: 290px;
    list-style: none; color: var(--ink-soft); font-size: 17px; line-height: 25px;
  }
  .contacts li { display: flex; align-items: center; }
  .contacts svg { width: 15px; height: 15px; margin-right: 16px; fill: var(--ink-white); }
  .portrait {
    position: absolute; right: 0; top: 0; width: 290px; height: 432px;
    background:
      radial-gradient(ellipse 60% 45% at 55% 35%, rgba(236,190,160,0.55), transparent 70%),
      linear-gradient(180deg, var(--brand-pink-light) 0%, var(--brand-pink) 55%, var(--portrait-navy) 100%);
  }
  .web-address {
    position: absolute; left: 0; right: 0; top: 383px;
    text-align: center; color: var(--ink-soft);
    font-size: 17px; letter-spacing: 2.5px;
  }
</style>
</head>
<body>
  <section class="card card--front">
    <div class="brand-name">Dore Lumia</div>
    <div class="holder">
      <div class="holder__name">MARCO TAVARES</div>
      <div class="holder__role">CEO/FOUNDER</div>
    </div>
    <div class="address">
      <div>Av. Miradouro Azul, 57</div>
      <div>4400-512, Vila Serena</div>
    </div>
    <ul class="contacts">
      <li><svg viewBox="0 0 16 16"><path d="M3.6 1.2l2.3 2.6-1.2 1.8c.9 1.9 2.5 3.5 4.4 4.4l1.8-1.2 2.6 2.3-1.1 2.2C7 13.2 2.9 9.1 1.4 3.5z"/></svg>(+351) 200 555 014</li>
      <li><svg viewBox="0 0 16 16"><path d="M4 1h8v4H4zM1 6h14v6h-3v3H4v-3H1zm4 4v4h6v-4z"/></svg>(+351) 200 555 019</li>
      <li><svg viewBox="0 0 16 16"><path d="M1 3h14v10H1zm1.5 1.3V12h11V4.3L8 8.5z M2.8 4L8 7.6 13.2 4z"/></svg>geral@dorelumia.com</li>
      <li><svg viewBox="0 0 16 16"><path d="M8 1a7 7 0 100 14A7 7 0 008 1zm0 1.4c.8 0 1.7 1.5 2 3.8H6c.3-2.3 1.2-3.8 2-3.8zM2.5 7.4h2.4v1.2H2.5zm3.6 0h3.8v1.2H6.1zm5 0h2.4v1.2h-2.4zM6 9.8h4c-.3 2.3-1.2 3.8-2 3.8s-1.7-1.5-2-3.8z"/></svg>www.dorelumia.com</li>
    </ul>
    <div class="portrait" role="img" aria-label="Portrait photo of the founder in a dark suit and tie"></div>
  </section>

  <section class="card card--back">
    <div class="brand-name">Dore Lumia</div>
    <div class="web-address">www.dorelumia.com</div>
  </section>
</body>
</html>
```